Business Card design for construction company

I would like a business card design for a construction company - Harlow Constructions. I have attached the ai logo file for use. I would like the card to be very smart and clean and incorporate only white and the two colours in the logo. I would like the card to have two sides. One side can just have the logo, the other with the relevant information.

Target Market(s)

Building and Construction Clients

Industry/Entity Type

Business

Contact Information for Business Card

Name: Tom Pardoe
Company: Harlow Constructions Pty Limited
Address: 14 Mallee Crescent Carrow Vale 2093
Phone: 0427 531 068
Email: tomp@harlowbuild-example.com.au

Font styles to use
Serif
Sans Serif

Requirements
Must have
• Details noted above
• Logo as provided
• Colours as in logo
• Square edges
• A font that compliments the logo
Should not have
• Any colour other than white and those in logo
• Rounded edges

```html
<!DOCTYPE html>
<html lang="en">
<head>
<meta charset="utf-8">
<title>Harlow Constructions – Business Card</title>
<link rel="stylesheet" href="https://fonts.googleapis.com/css2?family=Michroma&display=swap">
<style>
  :root {
    --ink: #505050;
    --accent: #1b9ad6;
    --paper: #ffffff;
    --backdrop: #dcdcdc;
  }
  * { box-sizing: border-box; margin: 0; padding: 0; }
  html, body {
    width: 1200px;
    height: 1200px;
    overflow: hidden;
    background: var(--backdrop);
    font-family: "Michroma", "Helvetica Neue", Arial, sans-serif;
    color: var(--ink);
  }
  .card {
    position: absolute;
    left: 152px;
    width: 900px;
    height: 540px;
    background: var(--paper);
  }
  .card--front { top: 40px; }
  .card--back { top: 606px; }

  .wordmark {
    position: absolute;
    left: 0;
    right: 0;
    top: 240px;
    display: flex;
    align-items: center;
    justify-content: center;
    gap: 22px;
  }
  .wordmark__square {
    width: 22px;
    height: 22px;
    background: var(--accent);
  }
  .wordmark__name {
    font-size: 36px;
    letter-spacing: 0.05em;
    text-transform: uppercase;
    color: var(--ink);
    line-height: 1;
  }

  .holder-name {
    position: absolute;
    right: 78px;
    top: 78px;
    font-size: 44px;
    font-variant: small-caps;
    letter-spacing: 0.1em;
    line-height: 1;
    color: var(--ink);
  }

  .contact-list {
    position: absolute;
    left: 76px;
    top: 258px;
    list-style: none;
  }
  .contact-list__item {
    display: flex;
    align-items: center;
    height: 37px;
    margin-bottom: 17px;
  }
  .contact-list__icon {
    width: 37px;
    height: 37px;
    flex: none;
  }
  .contact-list__text {
    margin-left: 35px;
    font-size: 20px;
    font-variant: small-caps;
    letter-spacing: 0.14em;
    white-space: nowrap;
  }
  .contact-list__text--lower {
    text-transform: lowercase;
    font-size: 19px;
    letter-spacing: 0.1em;
  }
</style>
</head>
<body>

<section class="card card--front" aria-label="Card front">
  <div class="wordmark">
    <span class="wordmark__square"></span>
    <span class="wordmark__name">Harlow Constructions</span>
  </div>
</section>

<section class="card card--back" aria-label="Card back">
  <h1 class="holder-name">Tom Pardoe</h1>

  <ul class="contact-list">
    <li class="contact-list__item">
      <svg class="contact-list__icon" viewBox="0 0 40 40" aria-hidden="true">
        <circle cx="20" cy="20" r="20" fill="var(--accent)"/>
        <g fill="none" stroke="#fff" stroke-width="2">
          <circle cx="20" cy="20" r="10"/>
          <ellipse cx="20" cy="20" rx="4.5" ry="10"/>
          <line x1="10" y1="20" x2="30" y2="20"/>
        </g>
      </svg>
      <span class="contact-list__text">HARLOW CONSTRUCTIONS PTY LIMITED</span>
    </li>
    <li class="contact-list__item">
      <svg class="contact-list__icon" viewBox="0 0 40 40" aria-hidden="true">
        <circle cx="20" cy="20" r="20" fill="var(--accent)"/>
        <path d="M20 31c-5-6-8-10-8-14a8 8 0 0 1 16 0c0 4-3 8-8 14z" fill="#fff"/>
        <circle cx="20" cy="17" r="3" fill="var(--accent)"/>
      </svg>
      <span class="contact-list__text">14 Mallee Crescent Carrow Vale 2093</span>
    </li>
    <li class="contact-list__item">
      <svg class="contact-list__icon" viewBox="0 0 40 40" aria-hidden="true">
        <circle cx="20" cy="20" r="20" fill="var(--accent)"/>
        <path d="M13 10l4 0 2 5-3 2c1 3 4 6 7 7l2-3 5 2 0 4c0 1-1 2-2 2-9 0-17-8-17-17 0-1 1-2 2-2z" fill="#fff"/>
      </svg>
      <span class="contact-list__text">0427 531 068</span>
    </li>
    <li class="contact-list__item">
      <svg class="contact-list__icon" viewBox="0 0 40 40" aria-hidden="true">
        <circle cx="20" cy="20" r="20" fill="var(--accent)"/>
        <rect x="10" y="13" width="20" height="14" fill="#fff"/>
        <path d="M10 13l10 8 10-8M10 27l7-7M30 27l-7-7" fill="none" stroke="var(--accent)" stroke-width="1.6"/>
      </svg>
      <span class="contact-list__text contact-list__text--lower">tomp@harlowbuild-example.com.au</span>
    </li>
  </ul>
</section>

</body>
</html>
```